Flyer für Verkauf von Nähmaschinen, Stickmaschinen und Overlock
Zielgruppe
1. Verkauf von Nähmaschinen, Stickmaschinen und Overlock.
2. Unsere Onlineshop ist www.Kornblum-Versand.de
4. Eigene Meisterwerkstatt wo alle Fabrikate repariert werden.
5. Zielgruppe = 95% Frauen
Aufgabenstellung
1. Format: DIN Maxi (23,5 x 12,5 cm Querformat, 2 Seiten)
2. Das Design soll an unseren Onlineshop www.kornblum-versand.de angelehnt sein.
3. Der Flyer soll eine Werbeaktion zum Black Friday (SILVER MAPLE DAYS) werden. 20% auf alle Neuwaren mit Gutscheincode. Unter anderem soll auf der Rückseite auch noch unsere eigene Meisterwerkstatt gezeigt werden, damit potenzielle Kunden auch wissen das wir eine Werkstatt haben.

```html
<!DOCTYPE html>
<html lang="de">
<head>
<meta charset="utf-8">
<title>Silver Maple Days – Flyer</title>
<link rel="stylesheet" href="https://fonts.googleapis.com/css2?family=Anton&family=Poppins:wght@400;500;600;700;800&display=swap">
<style>
  :root {
    --red: #e31b23;
    --ink: #1e1c1c;
    --text: #222;
    --paper: #ffffff;
    --paper-shade: #ececec;
    --stage: #d4d4d4;
  }
  * { box-sizing: border-box; margin: 0; padding: 0; }
  html, body { width: 1200px; height: 1117px; overflow: hidden; }
  body { background: var(--stage); font-family: "Poppins", sans-serif; color: var(--text); position: relative; }

  .flyer-side {
    position: absolute; left: 172px; width: 857px; height: 457px;
    background: radial-gradient(ellipse at 50% 25%, var(--paper) 0%, #f4f4f5 55%, var(--paper-shade) 100%);
    overflow: hidden;
  }
  .front { top: 72px; }
  .back { top: 582px; }

  .headline {
    position: absolute; top: 30px; left: 0; width: 100%; text-align: center;
    font-family: "Anton", sans-serif; font-size: 93px; line-height: 1; color: var(--ink);
    letter-spacing: 4px;
  }
  .headline .accent { color: var(--red); }
  .offer {
    position: absolute; top: 126px; left: 0; width: 100%; text-align: center;
    font-size: 22.5px; font-weight: 500; color: var(--ink);
  }
  .offer strong { color: var(--red); font-weight: 700; }
  .product-showcase {
    position: absolute; left: 75px; top: 160px; width: 716px; height: 218px;
    border-radius: 14px;
    background:
      linear-gradient(90deg, #c9ced0 0%, #8e9a9c 22%, #e9eaeb 36%, #f7f7f7 50%, #dcdde0 64%, #f2f3f4 78%, #c4cbd0 100%);
  }
  .url-pill {
    position: absolute; left: 146px; top: 398px; width: 365px; height: 36px;
    background: var(--red); border-radius: 18px; color: #fff;
    display: flex; align-items: center; gap: 8px; padding-left: 12px;
    font-size: 19px; font-weight: 600;
  }
  .url-pill svg { flex: none; }

  .brand {
    position: absolute; display: flex; align-items: center; gap: 8px;
    color: var(--red); font-weight: 800; line-height: 0.95;
  }
  .brand .mark { background: var(--red); flex: none; }
  .front .brand { left: 548px; top: 393px; font-size: 23px; }
  .front .brand .mark { width: 26px; height: 26px; }
  .back .brand { left: 548px; top: 336px; font-size: 38px; }
  .back .brand .mark { width: 42px; height: 42px; }

  .section-title {
    position: absolute; left: 56px; top: 40px;
    font-family: "Anton", sans-serif; font-size: 43px; line-height: 1; color: var(--red);
  }
  .title-rule { position: absolute; left: 56px; top: 95px; width: 418px; height: 3px; background: var(--red); }
  .intro {
    position: absolute; left: 56px; top: 111px; width: 440px;
    font-size: 14.3px; line-height: 17.5px; color: var(--text);
  }
  .photo { position: absolute; width: 144px; height: 132px; }
  .photo-a { left: 524px; top: 31px; background: linear-gradient(160deg, #d9d9d9, #3f7fa6 70%, #2c6d93); }
  .photo-b { left: 681px; top: 31px; background: linear-gradient(160deg, #5d6b75, #b9c8d8 55%, #8c8a83); }
  .photo-c { left: 524px; top: 174px; background: linear-gradient(160deg, #e4e1dc, #b9b3ab 45%, #1b9b82 80%); }
  .photo-d { left: 681px; top: 174px; background: linear-gradient(160deg, #4a3b32, #dcdcdc 50%, #22705c); }

  .red-wave { position: absolute; left: 0; top: 0; }
  .contact {
    position: absolute; left: 56px; top: 328px; list-style: none;
    color: #fff; font-size: 20.5px; font-weight: 500; line-height: 30px;
  }
  .contact li { display: flex; align-items: center; gap: 6px; }
  .contact svg { flex: none; }
</style>
</head>
<body>

<section class="flyer-side front">
  <h1 class="headline">SILVER MAPLE <span class="accent">DAYS</span></h1>
  <p class="offer"><strong>20%</strong> auf alle Neuwaren mit Gutscheincode.</p>
  <div class="product-showcase" role="img" aria-label="Produktfoto: Nähmaschine, Overlock und Stickmaschine auf einem weißen Podest"></div>
  <div class="url-pill">
    <svg width="16" height="16" viewBox="0 0 16 16"><circle cx="8" cy="8" r="8" fill="#fff"/><g fill="none" stroke="#e31b23" stroke-width="1.1"><circle cx="8" cy="8" r="4.5"/><ellipse cx="8" cy="8" rx="2" ry="4.5"/><line x1="3.5" y1="8" x2="12.5" y2="8"/></g></svg>
    www.kornblum-versand.de
  </div>
  <div class="brand"><span>KORNBLUM<br>VERSAND</span><span class="mark"></span></div>
</section>

<section class="flyer-side back">
  <svg class="red-wave" width="857" height="457" viewBox="0 0 857 457">
    <path d="M0 326 C80 290 150 278 220 279 C360 282 470 340 562 457 L0 457 Z" fill="#e31b23"/>
  </svg>
  <h2 class="section-title">Werkstatt</h2>
  <div class="title-rule"></div>
  <p class="intro">Entdecken Sie unsere hauseigene Nähmaschinenwerkstatt, in der wir Reparaturen für alle Fabrikate anbieten.<br>Ob es sich um eine kleine Anpassung oder eine umfassende Überholung handelt, unser geschultes Team steht Ihnen zur Verfügung, um Ihre Nähmaschine wieder in Bestform zu bringen. Und das Beste daran? Wir bieten auch einen bequemen Versand- und Transportservice an, damit Ihre Nähmaschine schnell und sicher zu uns gelangt.</p>
  <div class="photo photo-a" role="img" aria-label="Hände justieren eine Nähmaschine auf der Werkbank"></div>
  <div class="photo photo-b" role="img" aria-label="Mechaniker prüft ein Maschinenteil in der Werkstatt"></div>
  <div class="photo photo-c" role="img" aria-label="Techniker repariert eine Overlock-Maschine"></div>
  <div class="photo photo-d" role="img" aria-label="Schraubendreher an einer geöffneten Overlock"></div>
  <ul class="contact">
    <li><svg width="18" height="18" viewBox="0 0 18 18"><circle cx="9" cy="9" r="9" fill="#fff"/><path d="M6 4.5l1.6 2.3-1 1.2c.6 1.3 1.6 2.3 2.9 2.9l1.2-1 2.3 1.6-.8 1.6c-3.4-.2-6.9-3.7-7.1-7.1z" fill="#e31b23"/></svg>+49 (0)8123 / 45 67</li>
    <li><svg width="18" height="18" viewBox="0 0 18 18"><circle cx="9" cy="9" r="9" fill="#fff"/><rect x="4.5" y="6" width="9" height="6.5" fill="none" stroke="#e31b23" stroke-width="1.1"/><path d="M4.5 6l4.5 3.6L13.5 6" fill="none" stroke="#e31b23" stroke-width="1.1"/></svg>&nbsp;info@kornblum-versand.de</li>
    <li><svg width="18" height="18" viewBox="0 0 18 18"><circle cx="9" cy="9" r="9" fill="#fff"/><g fill="none" stroke="#e31b23" stroke-width="1.1"><circle cx="9" cy="9" r="5"/><ellipse cx="9" cy="9" rx="2.2" ry="5"/><line x1="4" y1="9" x2="14" y2="9"/></g></svg>&nbsp;www.kornblum-versand.de</li>
  </ul>
  <div class="brand"><span>KORNBLUM<br>VERSAND</span><span class="mark"></span></div>
</section>

</body>
</html>
```